Vantrell Law Letterhead

We need a new letterhead design for a Law Firm. The address for the law firm is 4817 Larkspur Boulevard, Suite 250, Houston, Texas 77342. Phone Number: 832-619-3057; Fax Number: 832-407-1694. The logo is uploaded to the project.

```html
<!DOCTYPE html>
<html lang="en">
<head>
<meta charset="utf-8">
<title>Vantrell Law Letterhead</title>
<link rel="stylesheet" href="https://fonts.googleapis.com/css2?family=Open+Sans:wght@400;600&family=Lato:wght@400&display=swap">
<style>
  :root {
    --navy: #172a52;
    --navy-soft: #22386a;
    --red: #e31e24;
    --ink: #3f3f3f;
    --paper: #ffffff;
    --backdrop: #e4e5e7;
    --signature-tone: #c9ccd3;
  }
  * { margin: 0; padding: 0; box-sizing: border-box; }
  html, body { width: 1040px; height: 1200px; overflow: hidden; }
  body { background: var(--backdrop); font-family: "Open Sans", Arial, sans-serif; color: var(--ink); }

  .letterhead {
    position: absolute; left: 61px; top: 9px;
    width: 918px; height: 1182px;
    background: var(--paper);
    box-shadow: 0 4px 14px rgba(0,0,0,0.18);
    overflow: hidden;
  }

  .header-band {
    position: absolute; left: 0; top: 0; width: 100%; height: 52px;
    background: linear-gradient(90deg, var(--navy) 0%, var(--navy-soft) 60%, var(--navy) 100%);
  }
  .footer-band {
    position: absolute; left: 0; bottom: 0; width: 100%; height: 150px;
    background: linear-gradient(180deg, var(--navy-soft) 0%, var(--navy) 100%);
  }

  .brand {
    position: absolute; left: 500px; top: 100px;
    display: flex; align-items: center; gap: 14px;
  }
  .brand-dot { width: 50px; height: 50px; border-radius: 50%; background: var(--red); flex: none; }
  .brand-name {
    font-weight: 600; font-size: 36px; color: var(--navy);
    letter-spacing: 0.5px; white-space: nowrap;
  }

  .letter-line { position: absolute; left: 86px; width: 742px; font-size: 14.5px; }
  .issue-date { top: 241px; }
  .recipient { top: 276px; line-height: 17.5px; }
  .salutation { top: 378px; }
  .letter-body {
    position: absolute; left: 86px; top: 423px; width: 742px;
    font-size: 14.5px; line-height: 26.5px; text-align: justify; hyphens: auto;
  }
  .letter-body p + p { margin-top: 26.5px; }
  .closing { top: 822px; }
  .signature {
    position: absolute; left: 86px; top: 852px; width: 213px; height: 24px;
    background: linear-gradient(90deg, var(--signature-tone), #e3e5ea);
    border-radius: 12px; opacity: 0.8;
  }
  .signer-name { top: 895px; font-size: 17.5px; color: #2e2e2e; }
  .signer-title { top: 930px; }

  .footer-contact {
    position: absolute; left: 0; top: 1094px; width: 918px; height: 62px;
    font-family: "Lato", Arial, sans-serif; color: #fff; font-size: 17px; line-height: 21px;
  }
  .footer-address {
    position: absolute; right: 340px; top: 10px;
    display: flex; gap: 8px; align-items: flex-start; white-space: nowrap;
  }
  .footer-divider { position: absolute; left: 599px; top: 0; width: 1px; height: 60px; background: rgba(255,255,255,0.8); }
  .footer-lines { position: absolute; left: 631px; top: 8px; }
  .footer-line { display: flex; align-items: center; gap: 10px; }
  .icon { width: 18px; height: 18px; flex: none; }
</style>
</head>
<body>
<main class="letterhead">
  <div class="header-band" role="img" aria-label="Navy and red wave ornament across the top edge"></div>

  <div class="brand">
    <span class="brand-dot"></span>
    <span class="brand-name">Vantrell Law</span>
  </div>

  <p class="letter-line issue-date">Issuing Date: May 5, 2018</p>
  <p class="letter-line recipient">Name Of Employee Mr. XYZABC<br>Address of Employee<br>Address Line 2 etc..</p>
  <p class="letter-line salutation">Dear Mr.XYZABC</p>

  <div class="letter-body">
    <p>Lorem Ipsum has been the industry's standard dummy text ever since the 1500s, when an unknown printer took a galley of type and scrambled it to make a type specimen book. It has survived not only five centuries, but also the leap into electronic typesetting, remaining essentially unchanged. It was popularised in the 1960s with the release of Letterfold sheets containing Lorem Ipsum passages, and more recently with desktop publishing software like Corvid PageSetter including versions of Lorem Ipsum.</p>
    <p>Lorem Ipsum is simply dummy text of the printing and typesetting industry. Lorem Ipsum has been the industry's standard dummy text ever since the 1500s, when an unknown printer took a galley of type and scrambled it to make a type specimen book.</p>
    <p>It has survived not only five centuries, but also the leap into electronic typesetting, remaining essentially unchanged. It was popularised in the 1960s with the release of Letterfold sheets containing Lorem IpsumIpsum passages.</p>
  </div>

  <p class="letter-line closing">Yours Sincerely</p>
  <div class="signature" role="img" aria-label="Handwritten signature of Marcus Hale"></div>
  <p class="letter-line signer-name">Marcus Hale</p>
  <p class="letter-line signer-title">Managing Director</p>

  <div class="footer-band" role="img" aria-label="Navy and red wave ornament across the bottom edge"></div>

  <footer class="footer-contact">
    <div class="footer-address">
      <svg class="icon" viewBox="0 0 24 24" aria-hidden="true"><path fill="#fff" d="M12 2C8.1 2 5 5.1 5 9c0 5.2 7 13 7 13s7-7.8 7-13c0-3.9-3.1-7-7-7zm0 9.5a2.5 2.5 0 1 1 0-5 2.5 2.5 0 0 1 0 5z"/></svg>
      <span>4817 Larkspur Boulevard, Suite 250<br>Houston, Texas 77342</span>
    </div>
    <span class="footer-divider"></span>
    <div class="footer-lines">
      <div class="footer-line">
        <svg class="icon" viewBox="0 0 24 24" aria-hidden="true"><path fill="#fff" d="M2 9c0-2 4-5 10-5s10 3 10 5v2h-5V8.5c-1.5-.6-3.2-.9-5-.9s-3.5.3-5 .9V11H2zM6 12h12l2 8H4z"/></svg>
        <span>832-619-3057</span>
      </div>
      <div class="footer-line">
        <svg class="icon" viewBox="0 0 24 24" aria-hidden="true"><path fill="#fff" d="M7 3h10v5H7zM3 9h18v8h-3v4H6v-4H3zm5 6v4h8v-4z"/></svg>
        <span>832-407-1694</span>
      </div>
    </div>
  </footer>
</main>
</body>
</html>
```